Carpentry company Needs a business card design

We need a design for a Carpentry / building company, business card. Please think of designs out of the ordinary and try to make it eye catching. Our existing logo will need to be incorporated in the design. However feel free to change the colours of the logo to suit your design. I would like to see some designs with green /black and orange incorporated into it.These are not the only colours accepted and all designs that appeal will be accepted.

Please contact me should you have any questions
Thanks Marcus

Target Market(s)

General Public seeking carpentry work

Industry/Entity Type

Business

Contact Information for Business Card

- Current company logo ( colours can be changed)
-Phone number ,
- info@brantelworks.com.au
- brantelworks.com.au
-the facebook symbol

Font styles to use
Other font styles liked:
• You choose

Requirements
Must have
• Services we provide
• - Renovations
• -Deckings & Pergolas
• -Kitchens
• - Bathrooms
• - Intricate details
Nice to have
• an awesome design
Should not have
• Tools on the business card

```html
<!DOCTYPE html>
<html lang="en">
<head>
<meta charset="utf-8">
<title>Brantel Works – Business Card</title>
<link rel="stylesheet" href="https://fonts.googleapis.com/css2?family=Michroma&family=Questrial&display=swap">
<style>
  :root {
    --backdrop: #dcdcdc;
    --card-light: #f1f1f1;
    --card-dark: #1c1011;
    --ink: #2a1d1e;
    --gold: #b47a2e;
    --muted: #8a8a8a;
    --light-text: #e4e0dd;
  }
  * { box-sizing: border-box; margin: 0; padding: 0; }
  html, body {
    width: 1105px;
    height: 1200px;
    overflow: hidden;
    background: var(--backdrop);
  }
  .card {
    position: absolute;
    left: 182px;
    width: 746px;
    height: 425px;
  }
  .card--front { top: 119px; background: var(--card-light); }
  .card--back { top: 637px; background: var(--card-dark); }

  .wordmark {
    position: absolute;
    left: 0;
    width: 100%;
    display: flex;
    align-items: center;
    justify-content: center;
    gap: 14px;
    font-family: "Michroma", sans-serif;
    font-size: 38px;
    letter-spacing: 2px;
    white-space: nowrap;
  }
  .wordmark__square { width: 16px; height: 16px; background: var(--gold); }
  .card--front .wordmark { top: 70px; color: var(--ink); justify-content: flex-start; padding-left: 190px; }
  .card--back .wordmark { top: 170px; color: var(--light-text); }

  .holder {
    position: absolute;
    right: 449px;
    top: 276px;
    text-align: right;
    font-family: "Michroma", sans-serif;
  }
  .holder__name { font-size: 19px; letter-spacing: 3px; color: var(--ink); line-height: 1.2; }
  .holder__role { font-size: 13px; letter-spacing: 3px; color: var(--gold); margin-top: 6px; }

  .divider {
    position: absolute;
    left: 297px;
    top: 251px;
    width: 1px;
    height: 104px;
    background: var(--muted);
  }

  .contacts {
    position: absolute;
    left: 330px;
    top: 245px;
    list-style: none;
    font-family: "Questrial", sans-serif;
    font-size: 19px;
    color: #3a3a3a;
  }
  .contacts__item {
    display: flex;
    align-items: center;
    gap: 12px;
    height: 29px;
  }
  .contacts__icon { width: 16px; height: 16px; flex: none; fill: var(--ink); }
  .contacts__square { width: 14px; height: 14px; margin: 0 1px; background: var(--ink); flex: none; }

  .services {
    position: absolute;
    top: 330px;
    left: 0;
    width: 100%;
    text-align: center;
    font-family: "Questrial", sans-serif;
    font-size: 19px;
    line-height: 32px;
    color: var(--light-text);
  }
  .services__sep { color: var(--gold); font-size: 12px; margin: 0 6px; vertical-align: 2px; }
</style>
</head>
<body>
  <section class="card card--front">
    <div class="wordmark"><span class="wordmark__square"></span>BRANTEL WORKS</div>

    <div class="holder">
      <p class="holder__name">MARCUS</p>
      <p class="holder__role">OWNER</p>
    </div>

    <div class="divider"></div>

    <ul class="contacts">
      <li class="contacts__item">
        <svg class="contacts__icon" viewBox="0 0 24 24" aria-hidden="true"><path d="M6.6 10.8a15 15 0 0 0 6.6 6.6l2.2-2.2a1 1 0 0 1 1-.25 11.4 11.4 0 0 0 3.6.57 1 1 0 0 1 1 1V20a1 1 0 0 1-1 1A17 17 0 0 1 3 4a1 1 0 0 1 1-1h3.5a1 1 0 0 1 1 1c0 1.25.2 2.45.57 3.57a1 1 0 0 1-.25 1z"/></svg>
        612 845 3071
      </li>
      <li class="contacts__item">
        <span class="contacts__square"></span>
        brantelworks
      </li>
      <li class="contacts__item">
        <svg class="contacts__icon" viewBox="0 0 24 24" aria-hidden="true"><path d="M2 5h20v14H2z M4 7v.4l8 5.2 8-5.2V7z" fill-rule="evenodd"/></svg>
        info@brantelworks.com.au
      </li>
      <li class="contacts__item">
        <svg class="contacts__icon" viewBox="0 0 24 24" aria-hidden="true"><circle cx="12" cy="12" r="10"/><path d="M12 2c3 3 3 17 0 20M12 2c-3 3-3 17 0 20M2 12h20" stroke="#f1f1f1" stroke-width="1.5" fill="none"/></svg>
        brantelworks.com.au
      </li>
    </ul>
  </section>

  <section class="card card--back">
    <div class="wordmark"><span class="wordmark__square"></span>BRANTEL WORKS</div>
    <div class="services">
      <p>Renovations <span class="services__sep">◆</span> Deckings &amp; Pergolas</p>
      <p>Kitchens <span class="services__sep">◆</span> Bathrooms <span class="services__sep">◆</span> Intricate details</p>
    </div>
  </section>
</body>
</html>
```